Stonelynk Business Card Design

The Stonelynk Co is an aggregate (crushing) equipment dealer serving Western Canadian provinces. Stonelynk is a distributor of aggregate equipment for different manufacturers.

We are looking to change and update the existing business card which has been used since the existence of the company. A copy of existing card has been attached for reference. The Stonelynk Co logo we want to remain the same and we want the green color to remain the same.

We are wanting something new with a different look. A refreshing card to show a new modern and updated look. No longer wanting to have the manufacturers on the back of the card but something more like our logo on the back of the card with a statement like "Crushing Solutions"

ideas could be:
- card can be different colors on front and back
- front or reverse of the card could possibly be the green color with the logo in black

Target Market(s)

Owners of Aggregate/Crushing companies

Requirements
Must have
• - logo to remain same along with same font within logo
• - green color to remain same
Nice to have
• as noted above under project description
Should not have

```html
<!DOCTYPE html>
<html lang="en">
<head>
<meta charset="utf-8">
<title>The Stonelynk Co – Business Card</title>
<link href="https://fonts.googleapis.com/css2?family=Montserrat:wght@400;500;700&display=swap" rel="stylesheet">
<style>
  :root {
    --stage: #a6a6a6;
    --brand-green: #8c9a1d;
    --brand-green-light: #a0ae2c;
    --charcoal: #2c2a2d;
    --ink: #1f1e20;
    --paper: #ffffff;
    --icon-green: #8c9a1d;
  }
  * { box-sizing: border-box; margin: 0; padding: 0; }
  html, body {
    width: 1200px; height: 1200px; overflow: hidden;
    background: var(--stage);
    font-family: "Montserrat", Arial, sans-serif;
  }
  .sheet {
    position: relative; width: 1200px; height: 1200px;
    display: flex; align-items: center; justify-content: center; gap: 50px;
  }
  .card {
    position: relative; width: 540px; height: 325px; overflow: hidden;
    background: var(--brand-green);
    box-shadow: 0 3px 10px rgba(0,0,0,.25);
  }
  .card::before {
    content: ""; position: absolute; inset: 0;
    background: radial-gradient(ellipse 60% 45% at 75% 20%, rgba(255,255,255,.10), transparent 70%),
                radial-gradient(ellipse 50% 35% at 80% 85%, rgba(255,255,255,.08), transparent 70%);
  }

  /* ---------- Contact side ---------- */
  .brand {
    position: absolute; display: flex; align-items: center; gap: 12px;
    font-weight: 700; letter-spacing: .2px; white-space: nowrap;
  }
  .brand-dot { border-radius: 50%; flex: none; }
  .card-front .brand { left: 26px; top: 30px; color: var(--ink); font-size: 17px; }
  .card-front .brand-dot { width: 26px; height: 26px; background: var(--ink); }

  .holder {
    position: absolute; right: 22px; top: 109px;
    font-size: 18px; color: var(--paper); letter-spacing: .3px;
  }
  .holder strong { font-weight: 700; }
  .holder span { font-weight: 400; }
  .holder-rule {
    position: absolute; left: 352px; right: 0; top: 134px;
    height: 2px; background: var(--charcoal);
  }
  .divider {
    position: absolute; left: 0; right: 0; top: 150px; height: 5px; background: var(--paper);
  }
  .divider-notch {
    position: absolute; left: 130px; top: 150px; width: 10px; height: 10px;
    background: var(--paper); transform: skewX(-30deg);
  }
  .contact-panel {
    position: absolute; left: 0; right: 0; top: 155px; bottom: 0; background: var(--charcoal);
  }
  .contact-panel + .divider-notch { z-index: 2; }

  .row {
    position: absolute; display: flex; align-items: center; gap: 10px;
    color: var(--paper); font-size: 14px; line-height: 1.2; letter-spacing: .2px;
  }
  .row.right { flex-direction: row-reverse; }
  .icon {
    width: 20px; height: 20px; border-radius: 50%; background: var(--icon-green);
    display: flex; align-items: center; justify-content: center; flex: none;
  }
  .icon svg { width: 12px; height: 12px; }
  .address { left: 22px; top: 173px; align-items: flex-start; }
  .address .icon { margin-top: 7px; }
  .phone-1 { left: 22px; top: 226px; }
  .phone-2 { left: 22px; top: 257px; }
  .phone-3 { left: 22px; top: 288px; }
  .email { right: 24px; top: 257px; }
  .web { right: 24px; top: 288px; }

  /* ---------- Logo side ---------- */
  .card-back .brand {
    left: 50%; top: 138px; transform: translateX(-50%);
    color: var(--paper); font-size: 19px;
  }
  .card-back .brand-dot { width: 30px; height: 30px; background: var(--paper); }
  .url-band {
    position: absolute; left: 0; right: 0; top: 282px; height: 17px;
    background: linear-gradient(90deg, rgba(44,42,45,0) 0%, var(--charcoal) 22%, var(--charcoal) 78%, rgba(44,42,45,0) 100%);
    display: flex; align-items: center; justify-content: center;
    color: var(--paper); font-size: 9.5px; letter-spacing: 2px; font-weight: 500;
  }
</style>
</head>
<body>
<main class="sheet">

  <section class="card card-front" aria-label="Business card contact side">
    <div class="brand"><span class="brand-dot"></span>THE STONELYNK CO.</div>

    <div class="holder"><strong>DALE</strong> <span>MORROW</span></div>
    <div class="holder-rule"></div>

    <div class="divider"></div>
    <div class="contact-panel"></div>
    <div class="divider-notch"></div>

    <div class="row address">
      <span class="icon"><svg viewBox="0 0 12 12"><path d="M6 1a3.3 3.3 0 0 0-3.3 3.3C2.7 7 6 11 6 11s3.3-4 3.3-6.7A3.3 3.3 0 0 0 6 1zm0 4.6a1.3 1.3 0 1 1 0-2.6 1.3 1.3 0 0 1 0 2.6z" fill="#2c2a2d"/></svg></span>
      <span>5512-72B AVENUE NISKU,<br>ALBERTA T9E1L8</span>
    </div>
    <div class="row phone-1">
      <span class="icon"><svg viewBox="0 0 12 12"><path d="M3 1.2l1.6 2.2-.9 1.1a6 6 0 0 0 3.8 3.8l1.1-.9 2.2 1.6-.9 1.8C6 10.6 1.4 6 1.2 2.1z" fill="#2c2a2d"/></svg></span>
      <span>780.555.0143</span>
    </div>
    <div class="row phone-2">
      <span class="icon"><svg viewBox="0 0 12 12"><path d="M3 1.2l1.6 2.2-.9 1.1a6 6 0 0 0 3.8 3.8l1.1-.9 2.2 1.6-.9 1.8C6 10.6 1.4 6 1.2 2.1z" fill="#2c2a2d"/></svg></span>
      <span>780.555.0187</span>
    </div>
    <div class="row phone-3">
      <span class="icon"><svg viewBox="0 0 12 12"><rect x="3.5" y="1" width="5" height="10" rx="1" fill="#2c2a2d"/><rect x="4.4" y="2.2" width="3.2" height="6" fill="#8c9a1d"/></svg></span>
      <span>780.555.0129</span>
    </div>
    <div class="row right email">
      <span class="icon"><svg viewBox="0 0 12 12"><rect x="1.5" y="3" width="9" height="6" fill="none" stroke="#2c2a2d" stroke-width="1.1"/><path d="M1.5 3L6 6.6 10.5 3" fill="none" stroke="#2c2a2d" stroke-width="1.1"/></svg></span>
      <span>DALE@STONELYNK.COM</span>
    </div>
    <div class="row right web">
      <span class="icon"><svg viewBox="0 0 12 12" fill="none" stroke="#2c2a2d" stroke-width="1"><circle cx="6" cy="6" r="4.5"/><ellipse cx="6" cy="6" rx="2" ry="4.5"/><path d="M1.5 6h9"/></svg></span>
      <span>WWW.STONELYNK.CA</span>
    </div>
  </section>

  <section class="card card-back" aria-label="Business card logo side">
    <div class="brand"><span class="brand-dot"></span>THE STONELYNK CO.</div>
    <div class="url-band">WWW.STONELYNK.CA</div>
  </section>

</main>
</body>
</html>
```